Birch Card Flyer

Please design a flyer with all the info on attached file. We want the logo in the upper left hand corner and a very simple and clean border. We want it to come across clean and modern. Please submit one with each of the four logos you made for us. Let me know if you have any questions.

```html
<!DOCTYPE html>
<html lang="en">
<head>
<meta charset="utf-8">
<title>Birch Card Flyer</title>
<link rel="stylesheet" href="https://fonts.googleapis.com/css2?family=Arimo:wght@400;500&display=swap">
<style>
  :root {
    --green: #a8d48c;
    --ink: #111111;
    --slate: #555559;
    --label: #666666;
    --frame: #6b6b6b;
    --paper: #ffffff;
  }
  * { margin: 0; padding: 0; box-sizing: border-box; }
  html, body { width: 1200px; height: 960px; overflow: hidden; background: var(--paper); }
  body { position: relative; font-family: "Arimo", Arial, sans-serif; color: var(--ink); }

  .side-label {
    position: absolute; top: 8px; width: 576px; text-align: center;
    font-size: 25px; color: var(--label);
  }
  .panel {
    position: absolute; top: 41px; width: 577px; height: 893px;
    border: 1px solid var(--frame); background: var(--paper); overflow: hidden;
  }
  .panel--front { left: 18px; }
  .panel--back { left: 607px; }
  .edge-band { position: absolute; left: 0; top: 0; bottom: 0; width: 35px; background: var(--green); }

  .brand-name {
    position: absolute; color: var(--slate); font-weight: 400; white-space: nowrap;
  }

  /* Front */
  .front-lockup .brand-name { left: 108px; top: 406px; font-size: 28px; }
  .front-lockup .divider { position: absolute; left: 238px; top: 374px; width: 1px; height: 92px; background: var(--slate); }
  .front-lockup .wordmark { position: absolute; left: 257px; top: 400px; font-size: 33px; color: var(--slate); white-space: nowrap; letter-spacing: -0.5px; }

  /* Back */
  .back-header .brand-name { left: 52px; top: 40px; font-size: 26px; }
  .site-link {
    position: absolute; left: 333px; top: 66px; font-size: 15px; color: var(--slate);
    padding-bottom: 3px; border-bottom: 1px solid var(--slate); white-space: nowrap;
  }
  .rule { position: absolute; left: 35px; right: 0; height: 2px; background: var(--green); }
  .rule--top { top: 108px; }
  .rule--bottom { top: 853px; }

  .title { position: absolute; left: 35px; right: 0; top: 130px; text-align: center; font-size: 39px; color: var(--slate); letter-spacing: -0.5px; font-weight: 400; }

  .intro { position: absolute; left: 71px; top: 211px; font-size: 16px; line-height: 47.5px; white-space: nowrap; }

  .benefits-banner {
    position: absolute; left: 35px; top: 475px; width: 402px; height: 36px;
    background: var(--green); color: var(--slate); font-size: 22px; line-height: 36px; padding-left: 36px; white-space: nowrap; font-weight: 400;
  }

  .benefits { position: absolute; left: 71px; top: 537px; list-style: none; font-size: 16px; line-height: 47.8px; }
  .benefits li { position: relative; padding-left: 31px; white-space: nowrap; }
  .benefits li::before { content: "*"; position: absolute; left: 0; top: -4px; font-size: 14px; }

  .footer-link { position: absolute; left: 35px; right: 0; top: 864px; text-align: center; font-size: 15px; color: var(--slate); }
</style>
</head>
<body>
  <div class="side-label" style="left:18px">Front</div>
  <div class="side-label" style="left:607px">Back</div>

  <section class="panel panel--front">
    <div class="edge-band"></div>
    <div class="front-lockup">
      <div class="brand-name">BIRCH</div>
      <div class="divider"></div>
      <div class="wordmark">The Birch Card</div>
    </div>
  </section>

  <section class="panel panel--back">
    <div class="edge-band"></div>
    <header class="back-header">
      <div class="brand-name">BIRCH</div>
      <div class="site-link">WWW.BIRCHCARDCLUB.COM</div>
    </header>
    <div class="rule rule--top"></div>

    <h1 class="title">The Birch Card</h1>

    <p class="intro">
      The Birch Card is Orange County’s Exclusive<br>
      Restaurant Loyalty Program.<br>
      We offer a unique marketing strategy, a strategy that<br>
      will help you gain new customers, increase traffic into<br>
      your restaurant and solidify a loyal customer base.
    </p>

    <h2 class="benefits-banner">How The Birch Card benefits you</h2>

    <ul class="benefits">
      <li>No Cost to your Restaurant</li>
      <li>Fill your tables with quality customers</li>
      <li>Free marketing and website exposure</li>
      <li>Gain new customers and solidify customer loyalty</li>
      <li>Increase traffic during your quiet periods</li>
      <li>Custom tailor options to fit your restaurants needs</li>
    </ul>

    <div class="rule rule--bottom"></div>
    <footer class="footer-link">WWW.BIRCHCARDCLUB.COM</footer>
  </section>
</body>
</html>
```